Tallow Electrical Business Card

We need a business card design for our family-run electrical contracting business based in Western Australia called 'Tallow Electrical'. We provide electrical services including residential, commercial and industrial. We aim for individual business cards to be made for all of our employees. We already have a company logo, which we require to be featured on the design. We would like simple, sleek and vibrant designs, which incorporate our logo and represent our business. We do not want anything involving too many graphics/images. We like the colours red, black, white and all shades of grey. The final design should communicate professionalism and trustworthiness.
We require the following contact information:
Name- Peter Hargreave
EC 5810
Mobile number- 0455 902 318
Fax number (including area code)- (08) 9576 2083
Email adress- name@tallowelectric.com.au
Industry/Entity Type
Electrical
Font styles to use
Other font styles liked:
- ITC Handel Bold
Look and feel

```html
<!DOCTYPE html>
<html lang="en">
<head>
<meta charset="utf-8">
<title>Tallow Electrical – Business Card</title>
<link rel="stylesheet" href="https://fonts.googleapis.com/css2?family=Days+One&display=swap">
<style>
  :root {
    --page: #ffffff;
    --card: #ffffff;
    --ink: #111111;
    --edge: #1a1a1a;
    --red: #ee2a2e;
    --grey: #7a7a7a;
  }
  * { box-sizing: border-box; margin: 0; padding: 0; }
  html, body {
    width: 1200px;
    height: 900px;
    overflow: hidden;
    background: var(--page);
  }
  .business-card {
    position: absolute;
    left: 32px;
    top: 92px;
    width: 1136px;
    height: 716px;
    background: var(--card);
    border: 2px solid var(--edge);
    border-radius: 3px;
    overflow: hidden;
    font-family: "Days One", "Arial Black", sans-serif;
    color: var(--ink);
  }
  .edge-stripes {
    position: absolute;
    top: 0;
    width: 60px;
    height: 100%;
  }
  .edge-stripes--left { left: 0; }
  .edge-stripes--right { right: 0; }

  .holder-name {
    position: absolute;
    left: 74px;
    top: 62px;
    font-size: 40px;
    letter-spacing: 0.5px;
  }
  .licence-number {
    position: absolute;
    left: 74px;
    top: 120px;
    font-size: 27px;
  }
  .company-mark {
    position: absolute;
    right: 76px;
    top: 66px;
    display: flex;
    align-items: center;
    gap: 14px;
  }
  .company-mark__square {
    width: 42px;
    height: 42px;
    background: var(--red);
  }
  .company-mark__name {
    font-size: 30px;
    color: var(--ink);
    letter-spacing: 1px;
  }
  .contact-list {
    position: absolute;
    left: 74px;
    top: 560px;
    list-style: none;
    font-size: 26px;
    line-height: 43px;
  }
</style>
</head>
<body>
  <article class="business-card">
    <svg class="edge-stripes edge-stripes--left" viewBox="0 0 60 716" preserveAspectRatio="none" aria-hidden="true">
      <rect x="0" y="0" width="24" height="716" fill="var(--red)"/>
      <rect x="26" y="0" width="10" height="716" fill="var(--grey)"/>
      <rect x="38" y="0" width="14" height="716" fill="var(--red)"/>
    </svg>

    <h1 class="holder-name">Peter Hargreave</h1>
    <p class="licence-number">EC 5810</p>

    <div class="company-mark">
      <span class="company-mark__square"></span>
      <span class="company-mark__name">TALLOW ELECTRICAL</span>
    </div>

    <ul class="contact-list">
      <li class="contact-item">Mobile number- 0455 902 318</li>
      <li class="contact-item">Fax number - (08) 9576 2083</li>
      <li class="contact-item">Email adress- name@tallowelectric.com.au</li>
    </ul>

    <svg class="edge-stripes edge-stripes--right" viewBox="0 0 60 716" preserveAspectRatio="none" aria-hidden="true">
      <rect x="0" y="0" width="12" height="716" fill="var(--grey)"/>
      <rect x="18" y="0" width="30" height="716" fill="var(--red)"/>
    </svg>
  </article>
</body>
</html>
```